Full Page Magazine Ad for Law Firm

Full Page Magazine Ad

The project is to design a full page ad to be place in Cannabis Harvest Quarterly magazine in the November 2017 edition.

Purpose of the ad is to promote Copperfield Ridge Law Group and not Martin Osgood from mo LAW ad.

About 20% of Copperfield Ridge Law Group’s current practice is marijuana related and it is looking grow that by illustrating in the ad that mo LAW is joining the firm.

Copperfield Ridge Law Group offers services in
• Tax Law
• Securities & Finance
• Business & Corporations
• Business Structuring
• Investments Funds & Management
• Rest Estate
• Outside General Counsel

mo LAW has offered services in:

• Marijuana regulation and compliance
• Buying and selling marijuana businesses
• Business & Corporations

Color palate should match Copperfield Ridge Law Group logo (blue) color with gray, black, white.

DO NOT want marijuana leaf images.
DO NOT include picture of Martin Osgood from mo LAW ad.

Documents provided:
Copperfield Ridge Law Group logo
Past mo LAW ad in magazine
Examples of competitor ads in same publication
Magazine spec sheet

Target Market(s)

The target of the ad is owners of larger marijuana retail stores and marijuana production/processing operations that need legal services.

Industry/Entity Type

Law Firm

Font styles to use
Other font styles liked:
• Should fit with CRLG logo.

Colors
3276b5

Requirements
Must have
• Copperfield Ridge Law Group is the Primary focus
• Use Copperfield Ridge Law Group address / contact information
• Ad must make clear that Copperfield Ridge Law Group is a Law Firm offering legal services to businesses.
Should not have
• DO NOT want marijuana leaf images.
• DO NOT include picture of Martin Osgood from mo LAW ad

```html
<!DOCTYPE html>
<html lang="en">
<head>
<meta charset="utf-8">
<title>Copperfield Ridge Law Group – Full Page Ad</title>
<link rel="stylesheet" href="https://fonts.googleapis.com/css2?family=Marcellus&family=Oswald:wght@400;500;600&family=Montserrat:wght@400;600&display=swap">
<style>
  :root {
    --brand-blue: #1d56a3;
    --brand-blue-dark: #123c7a;
    --brand-blue-bright: #3276b5;
    --accent-blue: #1f7ad6;
    --ink: #3a3a3a;
    --silver-light: #f4f4f4;
    --silver: #d4d4d4;
    --silver-dark: #8a8a8a;
    --black: #111111;
    --white: #ffffff;
    --backdrop: #8c8c8c;
  }
  * { box-sizing: border-box; margin: 0; padding: 0; }
  html, body { width: 1155px; height: 1200px; overflow: hidden; }
  body { background: var(--backdrop); position: relative; }

  .ad {
    position: absolute; left: 163px; top: 13px;
    width: 846px; height: 1198px;
    transform: scale(0.98); transform-origin: top left;
    background: var(--silver-light);
    overflow: hidden;
    box-shadow: 0 8px 24px rgba(0,0,0,.35);
  }
  .ad-shapes { position: absolute; inset: 0; width: 846px; height: 1198px; }

  .hero-photo {
    position: absolute; left: 0; top: 70px; width: 846px; height: 480px;
    background: radial-gradient(ellipse at 55% 55%, #7a3b26 0%, #b98a5c 30%, #e7dcc6 58%, #f3f1ee 80%);
  }

  .masthead {
    position: absolute; top: 34px; left: 0; width: 846px; text-align: center;
    font-family: "Marcellus", serif; font-weight: 400; color: var(--white);
    font-size: 37px; letter-spacing: 1px; white-space: nowrap;
  }
  .masthead small { font-size: 22px; letter-spacing: 1px; }

  .former-firm { position: absolute; left: 44px; top: 540px; width: 300px; color: var(--white); }
  .former-firm .kicker {
    font-family: "Oswald", sans-serif; font-weight: 500; font-size: 28px;
    color: #d9dde4; line-height: 1; letter-spacing: -0.3px; white-space: nowrap;
  }
  .former-firm .headline {
    font-family: "Oswald", sans-serif; font-weight: 600; font-size: 58px;
    line-height: 1.05; margin-top: 2px; white-space: nowrap; letter-spacing: -0.5px;
    background: linear-gradient(#ffffff 20%, #b9c0cb 90%);
    -webkit-background-clip: text; background-clip: text; color: transparent;
  }
  .rule-dotted { border-top: 1px dotted rgba(255,255,255,.7); margin-top: 12px; }

  .service-list { list-style: none; font-family: "Montserrat", sans-serif; }
  .service-list li { position: relative; padding-left: 26px; white-space: nowrap; }
  .service-list li svg { position: absolute; left: 0; width: 15px; height: 15px; }

  .former-firm .service-list { margin-top: 24px; font-size: 19px; line-height: 24px; color: var(--white); }
  .former-firm .service-list li { margin-bottom: 19px; white-space: normal; }
  .former-firm .service-list li svg { top: 5px; }

  .firm { position: absolute; left: 408px; top: 534px; width: 400px; }
  .firm-heading { font-weight: 400; }
  .firm .name-top {
    display: block; white-space: nowrap;
    font-family: "Oswald", sans-serif; font-weight: 500; font-size: 46px;
    color: var(--ink); line-height: 1.05; letter-spacing: -0.5px;
  }
  .firm .name-bottom {
    display: block; white-space: nowrap;
    font-family: "Oswald", sans-serif; font-weight: 600; font-size: 56px;
    color: var(--brand-blue); line-height: 1.05; letter-spacing: -0.5px;
  }
  .firm .rule-dotted { border-top-color: rgba(29,86,163,.7); margin-top: 6px; }
  .firm-pill {
    position: absolute; left: 383px; top: 686px; width: 400px; height: 42px;
    border-radius: 0 21px 21px 0;
    background: linear-gradient(#6d6d6d, #3c3c3c);
    box-shadow: 0 2px 3px rgba(0,0,0,.35);
    font-family: "Oswald", sans-serif; font-weight: 500; font-size: 21px;
    color: var(--white); line-height: 42px; padding-left: 24px; letter-spacing: -0.2px;
    white-space: nowrap;
  }
  .firm-services { position: absolute; left: 410px; top: 750px; font-size: 22px; color: var(--ink); }
  .firm-services li { line-height: 35px; }
  .firm-services li svg { top: 11px; }

  .contact-title {
    position: absolute; top: 1068px; left: 0; width: 846px; text-align: center;
    font-family: "Montserrat", sans-serif; font-weight: 600; font-size: 28px;
    color: var(--accent-blue); letter-spacing: 0.5px;
  }
  .phone-main {
    position: absolute; left: 44px; top: 1114px; display: flex; align-items: center; gap: 8px;
    font-family: "Oswald", sans-serif; font-weight: 500; font-size: 48px; color: #eeeeee;
    white-space: nowrap; letter-spacing: -0.5px; line-height: 1;
  }
  .phone-main svg { width: 38px; height: 48px; }
  .divider-vert { position: absolute; left: 418px; top: 1120px; width: 1px; height: 54px; background: #555; }
  .contact-details {
    position: absolute; left: 432px; top: 1122px; font-style: normal;
    font-family: "Oswald", sans-serif; font-size: 15px; color: #e6e6e6; line-height: 25px;
    white-space: nowrap;
  }
  .contact-details span { display: inline-flex; align-items: center; gap: 6px; margin-right: 12px; }
  .contact-details svg { width: 12px; height: 12px; }
</style>
</head>
<body>
<article class="ad">
  <div class="hero-photo" role="img" aria-label="Photograph of an engraved wooden gavel on its block beside stacked open law books and brass scales of justice"></div>

  <svg class="ad-shapes" viewBox="0 0 846 1198" aria-hidden="true">
    <defs>
      <linearGradient id="headerBlue" x1="0" y1="0" x2="0" y2="1">
        <stop offset="0" stop-color="#2a64b2"/><stop offset="1" stop-color="#1b4f98"/>
      </linearGradient>
      <linearGradient id="silverBand" x1="0" y1="0" x2="1" y2="0">
        <stop offset="0" stop-color="#4a4a4a"/><stop offset=".5" stop-color="#d8d8d8"/><stop offset="1" stop-color="#4a4a4a"/>
      </linearGradient>
      <linearGradient id="panelBlue" x1="0" y1="0" x2="0" y2="1">
        <stop offset="0" stop-color="#2158a6"/><stop offset=".7" stop-color="#1b4f98"/><stop offset="1" stop-color="#123c7a"/>
      </linearGradient>
      <linearGradient id="panelGray" x1="0" y1="0" x2="1" y2="1">
        <stop offset="0" stop-color="#ffffff"/><stop offset=".6" stop-color="#ececec"/><stop offset="1" stop-color="#d6d6d6"/>
      </linearGradient>
      <linearGradient id="footerBlack" x1="0" y1="0" x2="0" y2="1">
        <stop offset="0" stop-color="#2a2a2a"/><stop offset="1" stop-color="#0c0c0c"/>
      </linearGradient>
    </defs>

    <path d="M0 86 Q423 196 846 86 V102 Q423 214 0 102 Z" fill="url(#silverBand)"/>
    <path d="M0 0 H846 V76 Q423 204 0 76 Z" fill="url(#headerBlue)"/>
    <path d="M0 78 Q423 204 846 78" fill="none" stroke="#d9d9d9" stroke-width="6"/>

    <path d="M0 530 Q423 430 846 530 V1198 H0 Z" fill="url(#panelGray)"/>
    <path d="M0 526 Q423 424 846 526 V540 Q423 440 0 540 Z" fill="url(#silverBand)"/>
    <path d="M0 550 Q200 500 378 486 V850 Q378 960 326 1020 H0 Z" fill="url(#panelBlue)"/>
    <path d="M386 486 V850 Q386 964 334 1022" fill="none" stroke="#5a5a5a" stroke-width="5"/>

    <path d="M0 1050 Q320 985 846 1072 V1198 H0 Z" fill="#3a3a3a"/>
    <path d="M0 1062 Q320 998 846 1084 V1198 H0 Z" fill="url(#panelGray)"/>
    <rect x="0" y="1104" width="846" height="94" fill="url(#footerBlack)"/>
  </svg>

  <h1 class="masthead">COPPERFIELD RIDGE LAW GROUP <small>PLLC</small></h1>

  <section class="former-firm">
    <p class="kicker">MO LAW HAS OFFERED</p>
    <h2 class="headline">SERVICES IN</h2>
    <div class="rule-dotted"></div>
    <ul class="service-list">
      <li><svg viewBox="0 0 16 16"><circle cx="8" cy="8" r="7" fill="#6fa4e0"/><path d="M4.5 8.2 7 10.6 11.6 5.6" fill="none" stroke="#123c7a" stroke-width="2"/></svg>Marijuana regulation and compliance.</li>
      <li><svg viewBox="0 0 16 16"><circle cx="8" cy="8" r="7" fill="#6fa4e0"/><path d="M4.5 8.2 7 10.6 11.6 5.6" fill="none" stroke="#123c7a" stroke-width="2"/></svg>Buying and selling marijuana businesses.</li>
      <li><svg viewBox="0 0 16 16"><circle cx="8" cy="8" r="7" fill="#6fa4e0"/><path d="M4.5 8.2 7 10.6 11.6 5.6" fill="none" stroke="#123c7a" stroke-width="2"/></svg>Business &amp; Corporations</li>
    </ul>
  </section>

  <section class="firm">
    <h2 class="firm-heading"><span class="name-top">COPPERFIELD RIDGE</span><span class="name-bottom">LAW GROUP PLLC</span></h2>
    <div class="rule-dotted"></div>
  </section>
  <p class="firm-pill">COPPERFIELD RIDGE LAW GROUP SERVICES</p>
  <ul class="service-list firm-services">
    <li><svg viewBox="0 0 16 16"><circle cx="8" cy="8" r="7" fill="#1d56a3"/><path d="M4.5 8.2 7 10.6 11.6 5.6" fill="none" stroke="#fff" stroke-width="2"/></svg>Tax Law</li>
    <li><svg viewBox="0 0 16 16"><circle cx="8" cy="8" r="7" fill="#1d56a3"/><path d="M4.5 8.2 7 10.6 11.6 5.6" fill="none" stroke="#fff" stroke-width="2"/></svg>Securities &amp; Finance</li>
    <li><svg viewBox="0 0 16 16"><circle cx="8" cy="8" r="7" fill="#1d56a3"/><path d="M4.5 8.2 7 10.6 11.6 5.6" fill="none" stroke="#fff" stroke-width="2"/></svg>Business &amp; Corporations</li>
    <li><svg viewBox="0 0 16 16"><circle cx="8" cy="8" r="7" fill="#1d56a3"/><path d="M4.5 8.2 7 10.6 11.6 5.6" fill="none" stroke="#fff" stroke-width="2"/></svg>Business Structuring</li>
    <li><svg viewBox="0 0 16 16"><circle cx="8" cy="8" r="7" fill="#1d56a3"/><path d="M4.5 8.2 7 10.6 11.6 5.6" fill="none" stroke="#fff" stroke-width="2"/></svg>Investments Funds Management</li>
    <li><svg viewBox="0 0 16 16"><circle cx="8" cy="8" r="7" fill="#1d56a3"/><path d="M4.5 8.2 7 10.6 11.6 5.6" fill="none" stroke="#fff" stroke-width="2"/></svg>Rest Estate</li>
    <li><svg viewBox="0 0 16 16"><circle cx="8" cy="8" r="7" fill="#1d56a3"/><path d="M4.5 8.2 7 10.6 11.6 5.6" fill="none" stroke="#fff" stroke-width="2"/></svg>Outside General Counsel</li>
  </ul>

  <p class="contact-title">CONTACT US</p>
  <p class="phone-main">
    <svg viewBox="0 0 42 50" aria-hidden="true"><rect x="12" y="2" width="24" height="44" rx="4" fill="none" stroke="#eee" stroke-width="3"/><rect x="16" y="8" width="16" height="28" fill="#eee"/><circle cx="24" cy="41" r="2" fill="#eee"/><path d="M4 20 Q2 30 10 36" fill="none" stroke="#eee" stroke-width="3"/></svg>
    (503) 555-0148
  </p>
  <div class="divider-vert"></div>
  <address class="contact-details">
    <span><svg viewBox="0 0 12 12"><path d="M6 0a4 4 0 0 1 4 4c0 3-4 8-4 8S2 7 2 4a4 4 0 0 1 4-4z" fill="#eee"/><circle cx="6" cy="4" r="1.5" fill="#111"/></svg>480 Harbor Street, Suite 1200 Portland, Oregon 97204-3316</span><br>
    <span><svg viewBox="0 0 12 12"><rect x="0" y="2" width="12" height="8" fill="#eee"/><path d="M0 2 6 7 12 2" fill="none" stroke="#111" stroke-width="1"/></svg>Attys@CopperfieldRidge-Law.com</span>
    <span><svg viewBox="0 0 12 12"><rect x="0" y="5" width="12" height="7" fill="#eee"/><rect x="3" y="0" width="6" height="5" fill="#eee"/></svg>(503) 555-0149</span>
  </address>
</article>
</body>
</html>
```